5'x15' banner for sustainable apartments

Meadow 457 is a sustainable community that focuses on well being of tenants and reduction of carbon footprint.
Need an eye catching banner to be displayed on the side of a building. Walls are gray (see pic), so it's a perfect canvass to splash some colors. Banner shall include the word "apartments" and represent sustainability (ie. sustainable apartments).
Please check website to see more about the community: www.meadow457.example
Dimensions are 5' W x 15' H.
Daily traffic is approx. 20k cars.

Target Market(s)

we target environmentally conscious tenants who want to live in a community of like-minded people. We have a community garden, and reuse "gray" water for irrigation. We've also implemented recycling programs.
We've also built a deck were we have yoga practices -free of charge- for our tenants and guests.

Industry/Entity Type

Community

Font styles to use
Other font styles liked:
• Leelawadee UI

Requirements
Must have
• Should be understood that these are apartments for rent.
• whatever imagery is to be used, should have a strong association with sustainability.
• If any text, use Leelawadee UI font.
Nice to have
• well being imagery / association
• The picture with the painted mural is not from the subject building, but liked the drawing, so could spark some idea.

```html
<!DOCTYPE html>
<html lang="en">
<head>
<meta charset="utf-8">
<title>Meadow 457 – Apartments for Rent Banner</title>
<link rel="stylesheet" href="https://fonts.googleapis.com/css2?family=Bungee&family=Open+Sans:wght@400;600;700;800&display=swap">
<style>
  :root {
    --page: #ffffff;
    --slate: #4f5457;
    --body-bg: #eeefee;
    --lime: #7ed321;
    --lime-bright: #8ee62a;
    --lime-soft: #c6ef8c;
    --lime-pale: #e4f7c9;
    --ink: #3f4244;
    --muted: #9a9c9d;
    --white: #ffffff;
    --garden: #6e9a4a;
    --pool: #2a9ad8;
    --yoga: #8fb59a;
    --bike: #9a9c9e;
  }
  * { margin: 0; padding: 0; box-sizing: border-box; }
  html, body {
    width: 1200px; height: 3279px; overflow: hidden;
    background: var(--page);
    font-family: "Open Sans", "Leelawadee UI", sans-serif;
  }
  .canvas { position: relative; width: 1200px; height: 3279px; }
  .banner {
    position: absolute; left: 88px; top: 120px;
    width: 1013px; height: 3045px;
    background: var(--body-bg); overflow: hidden;
  }
  .backdrop {
    position: absolute; left: 0; top: 508px; width: 100%; height: 2332px;
    background: linear-gradient(100deg, var(--lime-soft) 0%, var(--lime-pale) 30%, var(--body-bg) 55%);
  }

  .header {
    position: absolute; left: 0; top: 0; width: 100%; height: 508px;
    background: var(--slate);
  }
  .brand-word, .brand-number {
    position: absolute; right: 95px;
    font-family: "Bungee", sans-serif; color: var(--lime-bright);
    line-height: 1; text-align: right;
  }
  .brand-word { top: 92px; font-size: 128px; letter-spacing: 2px; }
  .brand-number { top: 296px; font-size: 142px; }

  .headline {
    position: absolute; left: 0; width: 100%; text-align: center;
    padding-left: 20px;
  }
  .headline-main {
    top: 652px; font-family: "Bungee", sans-serif; font-size: 108px;
    color: var(--ink); letter-spacing: 1px;
  }
  .headline-sub {
    top: 800px; font-size: 88px; font-weight: 700; color: var(--lime);
    letter-spacing: -2px;
  }
  .call-line {
    position: absolute; top: 1036px; left: 0; width: 100%;
    text-align: center; padding-left: 60px;
    font-size: 52px; color: var(--lime);
  }
  .call-line .label { font-weight: 700; color: var(--muted); }
  .intro {
    position: absolute; top: 1240px; left: 148px; width: 720px;
    text-align: center; font-size: 28px; line-height: 1.5; color: var(--muted);
  }

  .feature { position: absolute; left: 140px; width: 820px; height: 250px; }
  .feature-photo {
    position: absolute; left: 0; top: 0;
    width: 244px; height: 244px; border-radius: 50%;
    border: 9px solid var(--lime-bright);
  }
  .feature-title {
    position: absolute; left: 304px; top: 8px;
    font-size: 38px; font-weight: 700; color: var(--lime); letter-spacing: 0.5px;
  }
  .feature-text {
    position: absolute; left: 304px; top: 80px; width: 460px;
    font-size: 22px; line-height: 1.5; color: var(--muted);
  }
  .f-garden { top: 1464px; }
  .f-pool   { top: 1740px; }
  .f-yoga   { top: 2016px; }
  .f-bike   { top: 2292px; }
  .f-garden .feature-photo { background: var(--garden); }
  .f-pool .feature-photo   { background: var(--pool); }
  .f-yoga .feature-photo   { background: var(--yoga); }
  .f-bike .feature-photo   { background: var(--bike); }

  .closing {
    position: absolute; top: 2628px; left: 0; width: 100%;
    text-align: center; padding-left: 20px; font-family: "Bungee", sans-serif;
    font-size: 58px; line-height: 1.35; color: var(--ink);
  }

  .footer {
    position: absolute; left: 0; bottom: 0; width: 100%; height: 205px;
    background: var(--slate); color: var(--white); text-align: center;
  }
  .footer-call {
    position: absolute; top: 6px; left: 0; width: 100%;
    font-size: 46px; letter-spacing: 1px;
  }
  .footer-call .label { color: var(--lime-bright); font-weight: 600; }
  .footer-social {
    position: absolute; top: 92px; left: 0; width: 100%;
    display: flex; justify-content: center; align-items: center; gap: 30px;
    font-size: 46px; letter-spacing: 1px;
  }
  .social-dot {
    width: 84px; height: 84px; border-radius: 50%; background: var(--lime-bright);
  }
</style>
</head>
<body>
<div class="canvas">
  <div class="banner">
    <div class="backdrop" role="img" aria-label="Decorative sweeping green bands with soft light circles"></div>

    <header class="header">
      <div class="brand-word">MEADOW</div>
      <div class="brand-number">457</div>
    </header>

    <h1 class="headline headline-main">APARTMENTS</h1>
    <h2 class="headline headline-sub">FOR RENT</h2>
    <p class="call-line"><span class="label">CALL:</span> XXX XXX XXX</p>
    <p class="intro">A community made by people for well-being and sustainable living</p>

    <section class="feature f-garden">
      <div class="feature-photo" role="img" aria-label="Photo of a smiling tenant in the community garden with fresh tomatoes"></div>
      <h3 class="feature-title">COMMUNITY GARDEN</h3>
      <p class="feature-text">Grow your own vegetables and herbs with your neighbours</p>
    </section>
    <section class="feature f-pool">
      <div class="feature-photo" role="img" aria-label="Photo of a person swimming underwater in the pool"></div>
      <h3 class="feature-title">POOL &amp; BBQ</h3>
      <p class="feature-text">Relax by the pool and share summer meals outdoors</p>
    </section>
    <section class="feature f-yoga">
      <div class="feature-photo" role="img" aria-label="Photo of a woman holding a rolled yoga mat outdoors"></div>
      <h3 class="feature-title">YOGA CLASSES</h3>
      <p class="feature-text">Free classes on our deck for tenants and guests</p>
    </section>
    <section class="feature f-bike">
      <div class="feature-photo" role="img" aria-label="Photo of a tenant with a bicycle in the bike storage"></div>
      <h3 class="feature-title">BIKE STORAGE</h3>
      <p class="feature-text">Secure indoor parking for bikes to ride green daily</p>
    </section>

    <p class="closing">WE OFFER MUCH MORE,<br>BOOK YOUR TOUR !</p>

    <footer class="footer">
      <p class="footer-call"><span class="label">CALL:</span> XXX XXX XXX</p>
      <p class="footer-social"><span class="social-dot"></span><span>MEADOW 457</span></p>
    </footer>
  </div>
</div>
</body>
</html>
```